Professional Letterhead for electronic use

I would like to inquire, if you could help me to create a letterhead, mostly for electronic use. Preferably in word file, with fixed letterhead design (header and footer), but will allow to add text on the main body of the letter. I usually operate online and would like to be able to add text, convert it to PDF and send as an attachment.
Target Market(s)
High net worth clients.
Industry/Entity Type
Real Estate Agent
Font styles to use
Other font styles liked:
- Century Gothic
Requirements
Must have
- Company name, logo, full address, email address, landline number, website address, Homestead Adjudicator logo, PELV logo, Company registration number
Nice to have
- Professional and elegant design

```html
<!DOCTYPE html>
<html lang="en">
<head>
<meta charset="utf-8">
<title>Corvane Estate Agents – Letterhead</title>
<link href="https://fonts.googleapis.com/css2?family=Questrial&display=swap" rel="stylesheet">
<style>
  :root {
    --backdrop: #ebebeb;
    --paper: #ffffff;
    --brand-orange: #e5521f;
    --brand-plum: #4a0f38;
    --footer-text: #e9dce4;
  }
  * { margin: 0; padding: 0; box-sizing: border-box; }
  html, body {
    width: 1200px;
    height: 898px;
    overflow: hidden;
    background: var(--backdrop);
    font-family: "Questrial", "Century Gothic", sans-serif;
  }
  .letterhead {
    position: absolute;
    left: 303px;
    top: 29px;
    width: 594px;
    height: 840px;
    background: var(--paper);
    box-shadow: 0 6px 24px rgba(0,0,0,0.12);
    overflow: hidden;
  }
  .brand {
    position: absolute;
    top: 52px;
    left: 0;
    width: 100%;
    display: flex;
    flex-direction: column;
    align-items: center;
  }
  .brand-dot {
    width: 44px;
    height: 44px;
    border-radius: 50%;
    background: var(--brand-orange);
    margin-bottom: 12px;
  }
  .brand-name {
    color: var(--brand-plum);
    font-size: 21px;
    letter-spacing: 5px;
    padding-left: 5px;
  }
  .brand-tagline {
    color: var(--brand-orange);
    font-size: 7.5px;
    letter-spacing: 3px;
    padding-left: 3px;
    margin-top: 4px;
  }
  .footer-bands {
    position: absolute;
    left: 0;
    bottom: 0;
    width: 594px;
    height: 250px;
    display: block;
  }
  .accreditations {
    position: absolute;
    right: 30px;
    bottom: 150px;
    display: flex;
    align-items: flex-end;
    gap: 12px;
  }
  .badge-adjudicator {
    width: 46px;
    height: 16px;
    background: var(--brand-orange);
  }
  .badge-pelv {
    width: 26px;
    height: 26px;
    border-radius: 50%;
    background: var(--brand-orange);
  }
  .contact-details {
    position: absolute;
    right: 30px;
    bottom: 40px;
    text-align: right;
    color: var(--footer-text);
    font-size: 7.5px;
    line-height: 1.5;
    letter-spacing: 0.6px;
  }
</style>
</head>
<body>
  <main class="letterhead">
    <header class="brand">
      <div class="brand-dot"></div>
      <div class="brand-name">CORVANE</div>
      <div class="brand-tagline">ESTATE AGENTS</div>
    </header>

    <svg class="footer-bands" viewBox="0 0 594 250" aria-hidden="true">
      <path d="M0,250 L0,195 Q300,70 594,20 L594,250 Z" fill="var(--brand-orange)"/>
      <path d="M0,250 L0,212 Q300,92 594,46 L594,250 Z" fill="var(--brand-plum)"/>
    </svg>

    <div class="accreditations">
      <div class="badge-adjudicator" role="img" aria-label="Homestead Adjudicator badge"></div>
      <div class="badge-pelv" role="img" aria-label="PELV badge"></div>
    </div>

    <footer class="contact-details">
      <p>214A Larkspur Road, Elmwood, London, NW9 4QT</p>
      <p>Sales Telephone 02071846320 Lettings Telephone 02071846320 Reg No. 07415538</p>
      <p>www.corvane.co.uk</p>
    </footer>
  </main>
</body>
</html>
```